Custom hot rod builder needs a website for launch of new business where he will build luxury garages

We need a website that gives a WOW first impression for "Summit Carhouses". This is a new business so photos are renderings but we need it to really attract a particular audience. Our initial business is custom hot rods so now we are building garages for them. These will be like luxury "homes" for cars! I will attach our new logo. Website needs to feel powerful and prestigious.

Target Market(s)

middle aged men, car enthusiasts

Industry/Entity Type

automotive, construction

Coding

Coded - Design and coding required

Number of Pages Required

2 page

Font styles to use
Serif

Colors
0054AA
0677BA
7BADD7
CADEEF
E8F1F8

Requirements
Must have
• a WOW factor. luxury. contact form.
Nice to have
• ?

```html
<!DOCTYPE html>
<html lang="en">
<head>
<meta charset="utf-8">
<title>Summit Carhouses</title>
<link rel="stylesheet" href="https://fonts.googleapis.com/css2?family=Cinzel:wght@400&family=Michroma&family=Montserrat:wght@400;500;600;700&display=swap">
<style>
:root{
  --blue-deep:#0054AA;
  --blue:#0677BA;
  --blue-bright:#1E9AE0;
  --blue-sky:#7BADD7;
  --blue-pale:#CADEEF;
  --blue-mist:#E8F1F8;
  --black:#000;
  --ink:#0a0a0a;
  --white:#fff;
  --grey:#c9c9c9;
}
*{box-sizing:border-box;margin:0;padding:0}
html,body{width:1200px;height:3465px;overflow:hidden;background:var(--black)}
body{position:relative;font-family:"Montserrat",Arial,sans-serif;color:var(--white)}
.abs{position:absolute}
.brand{display:flex;align-items:center;gap:12px;font-family:"Montserrat",Arial,sans-serif;font-weight:700;color:var(--blue-bright);letter-spacing:1px;line-height:1.05}
.brand-dot{width:46px;height:46px;border-radius:50%;background:var(--blue);flex:none}
.brand-name{font-size:22px}
.nav{position:absolute;top:32px;left:390px;display:flex;align-items:center;font-size:14px;letter-spacing:.3px}
.nav a{color:var(--white);text-decoration:none;margin-right:56px;padding-bottom:8px}
.nav a.active{border-bottom:2px solid var(--white)}
.nav .nav-cta{margin:0 0 0 -14px;border:2px solid var(--white);border-radius:20px;padding:10px 30px;margin-top:-8px}
.hero{left:0;top:0;width:1200px;height:753px;background:linear-gradient(180deg,#1e1f22 0%,#3a3d40 28%,#6f7478 48%,#8a8e8f 58%,#4e5a48 72%,#2b2e2a 86%,#000 100%)}
.eyebrow{font-family:"Montserrat",Arial,sans-serif;color:var(--blue-bright);letter-spacing:1.5px;text-transform:uppercase;font-size:15px;text-align:center}
.serif-title{font-family:"Cinzel",Georgia,serif;font-weight:400;color:var(--white);text-align:center;line-height:1}
.btn-outline{position:absolute;display:flex;align-items:center;justify-content:center;border:1.5px solid var(--white);font-family:"Michroma",Arial,sans-serif;font-size:10.5px;color:var(--blue-bright);letter-spacing:1px}
.body-copy{font-size:15px;line-height:23px;text-align:center;color:#eee}
.body-copy p+p{margin-top:12px}
.photo{position:absolute}
.why{left:0;top:1906px;width:1200px;height:589px;background:linear-gradient(180deg,#7d8da0 0%,#a9b3b7 25%,#5f6f4e 45%,#c9c8c2 60%,#bdbcb5 78%,#6c6c6a 100%)}
.feature{position:absolute;display:flex;gap:16px;align-items:flex-start}
.feature h3{font-size:17px;font-weight:600;color:var(--white);margin-bottom:4px}
.feature p{font-size:13.5px;line-height:19px;color:var(--blue-mist)}
.contact{left:0;top:2495px;width:1200px;height:639px}
.field{position:absolute;border:1.5px solid #e5e5e5;background:rgba(0,0,0,.35);color:#bbb;font-size:13px;padding:15px 20px}
.submit{position:absolute;left:534px;top:2852px;width:161px;height:42px;border-radius:21px;background:var(--blue-bright);font-family:"Michroma",Arial,sans-serif;font-size:13px;display:flex;align-items:center;justify-content:center;letter-spacing:1px}
.footer-rule{position:absolute;top:3201px;width:1.5px;height:202px;background:#333}
.footer-head{position:absolute;font-size:15px;font-weight:600;padding-left:16px;border-left:2px solid var(--blue-bright);margin-left:-16px}
.footer-link{position:absolute;font-size:12px;color:#ddd}
.contact-row{position:absolute;display:flex;align-items:center;gap:12px;font-size:12px;line-height:15px}
.icon-dot{width:27px;height:27px;border-radius:50%;background:var(--blue-bright);display:flex;align-items:center;justify-content:center;flex:none}
.social{position:absolute;top:3296px;width:28px;height:28px;border-radius:50%;border:3px solid var(--white)}
</style>
</head>
<body>

<!-- Hero -->
<section class="abs hero" role="img" aria-label="Evening rendering of a modern glass-fronted car garage with classic cars on display, palm trees and hedges"></section>
<header>
  <div class="abs brand" style="left:113px;top:26px"><span class="brand-dot"></span><span class="brand-name">SUMMIT<br>CARHOUSES</span></div>
  <nav class="nav">
    <a class="active">HOME</a><a>ABOUT GARAGE</a><a>SERVICES</a><a>GARAGE CARS</a><a class="nav-cta">CONTACT US</a>
  </nav>
</header>
<div class="abs eyebrow" style="left:0;width:1200px;top:164px;font-family:'Cinzel',Georgia,serif;font-size:34px;letter-spacing:0;text-transform:uppercase">Welcome to</div>
<h1 class="abs serif-title" style="left:0;width:1200px;top:198px;font-size:70px">SUMMIT CARHOUSES</h1>
<div class="btn-outline" style="left:517px;top:284px;width:169px;height:41px">EXPLORE MORE</div>
<svg class="abs" style="left:54px;top:296px" width="30" height="56" viewBox="0 0 30 56"><path d="M28 2 2 28l26 26" fill="none" stroke="#fff" stroke-width="2"/></svg>
<svg class="abs" style="left:1116px;top:296px" width="30" height="56" viewBox="0 0 30 56"><path d="M2 2l26 26L2 54" fill="none" stroke="#fff" stroke-width="2"/></svg>
<svg class="abs" style="left:603px;top:670px" width="26" height="38" viewBox="0 0 26 38"><path d="M13 1v35M2 25l11 11 11-11" fill="none" stroke="#fff" stroke-width="2"/></svg>

<!-- About -->
<div class="photo" style="left:67px;top:773px;width:628px;height:448px;background:radial-gradient(ellipse at 45% 45%,#8c7a55 0%,#4c4a44 35%,#1b1c1d 70%,#000 100%)" role="img" aria-label="Close view of the garage showroom windows with cars inside"></div>
<div class="abs eyebrow" style="left:632px;width:452px;top:831px">Summit Carhouse</div>
<h2 class="abs serif-title" style="left:632px;width:452px;top:852px;font-size:56px">ABOUT US</h2>
<div class="abs body-copy" style="left:628px;width:460px;top:918px">
  <p>Lorem ipsum dolor sit amet, consectetur adipiscing elit, sed do eiusmod tempor incididunt ut labore et dolore magna aliqua. Ut enim ad minim veniam, quis nostrud exercitation ullamco laboris nisi ut aliquip ex ea commodo consequat.</p>
  <p>Duis aute irure dolor in reprehenderit in voluptate velit esse cillum dolore eu fugiat nulla pariatur.</p>
</div>
<div class="btn-outline" style="left:773px;top:1095px;width:170px;height:42px">LEARN MORE</div>

<!-- Our garage -->
<div class="abs eyebrow" style="left:120px;width:472px;top:1387px">Summit Carhouse</div>
<h2 class="abs serif-title" style="left:120px;width:472px;top:1407px;font-size:54px">OUR GARAGE</h2>
<div class="abs body-copy" style="left:126px;width:460px;top:1474px">
  <p>Lorem ipsum dolor sit amet, consectetur adipiscing elit, sed do eiusmod tempor incididunt ut labore et dolore magna aliqua. Ut enim ad minim veniam, quis nostrud exercitation ullamco laboris nisi ut aliquip ex ea commodo consequat.</p>
  <p>Duis aute irure dolor in reprehenderit in voluptate velit esse cillum dolore eu fugiat nulla pariatur.</p>
</div>
<div class="btn-outline" style="left:272px;top:1649px;width:169px;height:42px">LEARN MORE</div>
<div class="abs" style="left:612px;top:1406px;width:249px;height:282px;border:10px solid var(--blue-bright);border-right:none;border-top-width:10px"></div>
<div class="photo" style="left:638px;top:1306px;width:424px;height:352px;background:linear-gradient(160deg,#8a5a38 0%,#5a3a26 35%,#2e3a38 65%,#1c2a2a 100%)" role="img" aria-label="Interior of the garage lounge with wood ceiling, artwork and a teal classic car"></div>
<div class="photo" style="left:870px;top:1501px;width:330px;height:285px;background:linear-gradient(180deg,#cfd3d6 0%,#b8bcbe 30%,#6b5a3a 55%,#c9a640 75%,#3a3a36 100%)" role="img" aria-label="Garage facade with large windows showing yellow sports cars and a motorcycle"></div>
<div class="abs" style="left:605px;top:1870px;width:2px;height:36px;background:var(--blue-bright)"></div>

<!-- Why -->
<section class="abs why" role="img" aria-label="Daytime rendering of the garage exterior with classic cars behind glass and a paved forecourt"></section>
<svg class="abs" style="left:0;top:1906px" width="1200" height="589" viewBox="0 0 1200 589" aria-hidden="true">
  <defs><linearGradient id="whyBlue" x1="0" y1="0" x2="0.4" y2="1"><stop offset="0" stop-color="#0677BA"/><stop offset="1" stop-color="#5cc6ee"/></linearGradient></defs>
  <polygon points="656,0 1200,0 1200,589 430,589" fill="url(#whyBlue)"/>
</svg>
<div class="abs eyebrow" style="left:670px;top:1985px;color:var(--blue-mist);text-align:left">Summit Carhouse</div>
<h2 class="abs serif-title" style="left:666px;top:2006px;font-size:45px;text-align:left">WHY OUR GARAGE</h2>
<div class="feature" style="left:660px;top:2076px">
  <svg width="72" height="86" viewBox="0 0 72 86"><path d="M8 26a32 32 0 0 1 56 0M8 60a32 32 0 0 0 56 0" fill="none" stroke="#fff" stroke-width="4"/><path d="M20 38 36 28l16 10v20H20z" fill="none" stroke="#fff" stroke-width="3"/><rect x="28" y="44" width="16" height="14" fill="none" stroke="#fff" stroke-width="2.5"/></svg>
  <div style="padding-top:16px"><h3>CAR GARAGE</h3><p>consectetur adipiscing elit, sed do eiusmod tempor<br>incididunt consectetur adipiscing elit sed do</p></div>
</div>
<div class="feature" style="left:660px;top:2188px">
  <svg width="72" height="86" viewBox="0 0 72 86"><path d="M8 26a32 32 0 0 1 56 0M8 60a32 32 0 0 0 56 0" fill="none" stroke="#fff" stroke-width="4"/><path d="M12 48v-6l8-2 6-7h18l8 7 8 2v6z" fill="none" stroke="#fff" stroke-width="3"/><circle cx="22" cy="49" r="4" fill="#fff"/><circle cx="50" cy="49" r="4" fill="#fff"/></svg>
  <div style="padding-top:16px"><h3>CAR GARAGE</h3><p>consectetur adipiscing elit, sed do eiusmod tempor<br>incididunt consectetur adipiscing elit sed do</p></div>
</div>
<div class="feature" style="left:652px;top:2302px">
  <svg width="72" height="86" viewBox="0 0 72 86"><path d="M8 26a32 32 0 0 1 56 0M8 60a32 32 0 0 0 56 0" fill="none" stroke="#fff" stroke-width="4"/><circle cx="36" cy="43" r="13" fill="none" stroke="#fff" stroke-width="3" stroke-dasharray="5 3"/><circle cx="36" cy="43" r="5" fill="none" stroke="#fff" stroke-width="3"/><path d="M44 51l10 10" stroke="#fff" stroke-width="4"/></svg>
  <div style="padding-top:16px"><h3>CAR GARAGE</h3><p>consectetur adipiscing elit, sed do eiusmod tempor<br>incididunt consectetur adipiscing elit sed do</p></div>
</div>

<!-- Contact -->
<section class="abs contact" role="img" aria-label="Monochrome night rendering of the garage facade behind the contact form" style="background:linear-gradient(180deg,#000 0%,#0d0d0d 20%,#2a2a2a 55%,#3b3b3b 75%,#1a1a1a 100%)"></section>
<div class="abs" style="left:0;width:1200px;top:2561px;text-align:center;font-size:15px;letter-spacing:1.5px;color:#ddd">GET IN TOUCH</div>
<h2 class="abs" style="left:0;width:1200px;top:2576px;text-align:center;font-family:'Michroma',Arial,sans-serif;font-size:31px;font-weight:400;letter-spacing:2px">CONTACT US</h2>
<div class="field" style="left:253px;top:2635px;width:354px;height:46px">First Name</div>
<div class="field" style="left:617px;top:2635px;width:354px;height:46px">Last Name</div>
<div class="field" style="left:253px;top:2693px;width:354px;height:46px">Email address</div>
<div class="field" style="left:617px;top:2693px;width:354px;height:46px">Phone</div>
<div class="field" style="left:253px;top:2751px;width:718px;height:76px;padding-left:28px">Leave Message</div>
<div class="submit">SUBMIT</div>

<!-- Footer -->
<footer>
  <div class="abs brand" style="left:118px;top:3270px"><span class="brand-dot"></span><span class="brand-name">SUMMIT<br>CARHOUSES</span></div>
  <div class="abs" style="left:118px;top:3353px;font-size:12.5px;line-height:19px">Copyright © 2022 Summit Carhouse<br>All Rights Reserved</div>
  <div class="footer-rule" style="left:403px"></div>
  <div class="footer-rule" style="left:621px"></div>
  <div class="footer-rule" style="left:892px"></div>
  <div class="footer-head" style="left:421px;top:3262px">NAVIGATION</div>
  <div class="footer-link" style="left:421px;top:3294px">About Us</div>
  <div class="footer-link" style="left:421px;top:3321px">Our Services</div>
  <div class="footer-link" style="left:421px;top:3348px">Garage Cars</div>
  <div class="footer-link" style="left:421px;top:3374px">Contact Us</div>
  <div class="footer-head" style="left:640px;top:3262px">CONTACT US</div>
  <div class="contact-row" style="left:640px;top:3297px"><span class="icon-dot"><svg width="12" height="16" viewBox="0 0 12 16"><path d="M6 15S1 9 1 6a5 5 0 0 1 10 0c0 3-5 9-5 9z" fill="#fff"/><circle cx="6" cy="6" r="2" fill="#1E9AE0"/></svg></span><span>418 Ridgecrest Lane<br>Millbrook, Ohio 43120</span></div>
  <div class="contact-row" style="left:640px;top:3340px;font-weight:600"><span class="icon-dot"><svg width="14" height="14" viewBox="0 0 14 14"><path d="M3 1l3 3-2 2a8 8 0 0 0 4 4l2-2 3 3-2 2C6 13 1 8 1 3z" fill="#fff"/></svg></span><span>(555) 318 2047</span></div>
  <div class="contact-row" style="left:640px;top:3373px"><span class="icon-dot"><svg width="14" height="10" viewBox="0 0 14 10"><rect x="0.5" y="0.5" width="13" height="9" fill="none" stroke="#fff"/><path d="M1 1l6 5 6-5" fill="none" stroke="#fff"/></svg></span><span>hello@summitcarhouses.com</span></div>
  <div class="footer-head" style="left:911px;top:3262px">GET IN TOUCH</div>
  <div class="social" style="left:911px"></div>
  <div class="social" style="left:945px"></div>
  <div class="social" style="left:979px"></div>
  <div class="social" style="left:1013px"></div>
</footer>

</body>
</html>
```